Infographic for venture capital "investment adviser" model

We need an infographic for users to easily visualize and grasp what is meant by a "investment adviser" model. The attached .pdf has the copy and my (very bad) rough design of the graphic. Needs to be professionally done now.

Description of Venture Capital: a venture capitalist creates a "fund", they then go raise money from investors for that fund. Once they have money, they then invest it in various companies or assets. As money com comes back to the fund from the investments, the venture capitalist pays the funds investors (and themselves).

A venture capitalist will usually manage multiple "funds". That's why there is a management company (the VC) that is hired by each fund they create. The VC management company is paid an annual fee of 2%, and then they also get 20% of the profits - that's what the "2%/20%" represents in the graphic.

Target Market(s)

Venture capitalists, investment advisers, wall street brokers

Industry/Entity Type

Venture Capital

Font styles to use
Serif

Colors
f37122
f68d4c
3276b5

Requirements
Must have
• Our logo (attached)
• Display 3 different funds, all being managed by a single entity
• Fyi - I just uploaded a new graphic of what the "website" should look like (can be similar, doesn't have to be this image...just something to show a crowdfunding website)
Nice to have
• Neat representations of investors and of a funds portfolio companies

```html
<!DOCTYPE html>
<html lang="en">
<head>
<meta charset="utf-8">
<title>Funding Platform – VC Investment Adviser Model</title>
<link href="https://fonts.googleapis.com/css2?family=Open+Sans:wght@600;700;800&family=Merriweather:ital,wght@0,400;0,700;0,900;1,400;1,700&display=swap" rel="stylesheet">
<style>
  :root{
    --orange:#f37122;
    --orange-soft:#f68d4c;
    --frame:#f4a46a;
    --blue:#3276b5;
    --blue-deep:#2c6aa5;
    --ink:#1c1c1c;
    --grey:#8a8a8a;
    --white:#ffffff;
  }
  *{box-sizing:border-box;margin:0;padding:0}
  html,body{width:1200px;height:857px;overflow:hidden;background:var(--white)}
  .canvas{position:relative;width:1200px;height:857px;background:var(--white);border:10px solid var(--frame);font-family:"Merriweather",Georgia,serif;color:var(--ink)}
  .header{position:absolute;left:14px;top:14px;width:1152px;height:86px;display:flex}
  .header-title{width:570px;background:var(--blue);color:var(--white);font-family:"Open Sans",Arial,sans-serif;font-weight:800;font-size:50px;letter-spacing:1px;display:flex;align-items:center;justify-content:center}
  .header-sub{flex:1;background:var(--orange);color:var(--white);font-family:"Merriweather",Georgia,serif;font-weight:700;font-size:31px;display:flex;align-items:center;padding-left:16px}
  .diagram{position:absolute;left:0;top:0}
  .box{position:absolute;border-radius:14px;box-shadow:3px 4px 6px rgba(0,0,0,.35)}
  .ventures{left:510px;top:116px;width:205px;height:86px;background:var(--orange);border:3px solid var(--white);outline:1px solid #ccc;text-align:center;padding-top:5px}
  .ventures h2{font-weight:900;font-size:20px;line-height:1.1}
  .ventures h3{font-weight:700;font-size:14px;line-height:1.25}
  .ventures p{font-style:italic;font-size:11.5px;line-height:1.35}
  .website{left:80px;top:343px;width:188px;height:124px;background:var(--white);border:3px solid var(--grey);padding:10px 12px}
  .website h2,.broker h2{font-weight:700;font-size:14.5px;line-height:1.3}
  .website h2 em{font-style:italic}
  .fn-label{font-style:italic;font-size:12.5px;margin-top:2px}
  .fn-list{list-style:none;font-family:"Open Sans",Arial,sans-serif;font-weight:700;font-size:13px;line-height:1.6}
  .fn-list li::before{content:"";display:inline-block;width:9px;height:9px;border-radius:50%;background:var(--orange-soft);margin-right:7px}
  .broker{left:932px;top:623px;width:168px;height:190px;background:var(--white);border:3px solid var(--grey);padding:10px 12px}
  .broker h2{text-align:center}
  .brand{display:flex;align-items:center;gap:5px;margin:2px 0 4px;font-family:"Open Sans",Arial,sans-serif;font-weight:800;font-size:17px;color:var(--blue-deep)}
  .brand-mark{width:10px;height:10px;background:var(--orange)}
  .broker .fn-list{font-size:12px;line-height:1.62}
  .fund-label{position:absolute;left:170px;top:640px;font-family:"Open Sans",Arial,sans-serif;font-weight:700;font-size:18px}
  .investors-label{position:absolute;font-family:"Merriweather",Georgia,serif;font-size:13px;color:var(--orange)}
  .note{position:absolute;left:36px;top:790px;font-family:"Open Sans",Arial,sans-serif;font-weight:700;font-size:11.5px;color:var(--orange)}
  .note u{text-decoration:underline}
  .copyright{position:absolute;left:33px;top:808px;font-family:"Open Sans",Arial,sans-serif;font-weight:600;font-size:11.5px}
  .flow-text{font-family:"Open Sans",Arial,sans-serif;font-weight:700;fill:var(--ink)}
</style>
</head>
<body>
<div class="canvas">
  <header class="header">
    <div class="header-title">FUNDING PLATFORM</div>
    <div class="header-sub">VC “Investment !dviser” Model *</div>
  </header>

  <svg class="diagram" width="1180" height="837" viewBox="0 0 1180 837">
    <defs>
      <marker id="head" viewBox="0 0 10 10" refX="9" refY="5" markerWidth="7" markerHeight="7" orient="auto-start-reverse">
        <path d="M0,0 L10,5 L0,10 z" fill="#1c1c1c"/>
      </marker>
    </defs>
    <g stroke="#1c1c1c" stroke-width="1.6" fill="none" marker-end="url(#head)">
      <!-- fees to management group -->
      <line x1="370" y1="598" x2="538" y2="207"/>
      <line x1="604" y1="605" x2="604" y2="207"/>
      <line x1="778" y1="602" x2="680" y2="207"/>
      <!-- technology & marketing to website -->
      <line x1="345" y1="602" x2="262" y2="482"/>
      <line x1="530" y1="622" x2="262" y2="462"/>
      <line x1="750" y1="618" x2="273" y2="428"/>
      <!-- funds to portfolio -->
      <line x1="308" y1="660" x2="290" y2="697"/>
      <line x1="548" y1="682" x2="530" y2="700"/>
      <line x1="790" y1="690" x2="770" y2="727"/>
      <!-- broker-dealer links -->
      <line x1="930" y1="638" x2="880" y2="638"/>
      <line x1="545" y1="713" x2="926" y2="688"/>
      <line x1="672" y1="728" x2="926" y2="696"/>
      <line x1="893" y1="742" x2="928" y2="712"/>
    </g>
    <g stroke="#1c1c1c" stroke-width="1.6" fill="none" marker-start="url(#head)" marker-end="url(#head)">
      <line x1="393" y1="690" x2="420" y2="720"/>
      <line x1="618" y1="690" x2="632" y2="720"/>
      <line x1="860" y1="693" x2="872" y2="723"/>
    </g>

    <text class="flow-text" font-size="21" transform="translate(478 300) rotate(-67)" text-anchor="middle">2%/20%</text>
    <text class="flow-text" font-size="21" transform="translate(597 300) rotate(-90)" text-anchor="middle">2%/20%</text>
    <text class="flow-text" font-size="21" transform="translate(704 315) rotate(-76)" text-anchor="middle">2%/20%</text>
    <text class="flow-text" font-size="12.5" transform="translate(312 535) rotate(56)" text-anchor="middle">Technology &amp; Mktg</text>
    <text class="flow-text" font-size="12.5" transform="translate(338 490) rotate(31)" text-anchor="middle">Technology &amp; Mktg</text>
    <text class="flow-text" font-size="12.5" transform="translate(502 500) rotate(22)" text-anchor="middle">Technology &amp; Mktg</text>

    <g fill="var(--blue-deep)">
      <ellipse cx="358" cy="648" rx="78" ry="40"/>
      <ellipse cx="602" cy="648" rx="78" ry="40"/>
      <ellipse cx="800" cy="648" rx="78" ry="40"/>
    </g>
    <g fill="#ffffff" font-family="Merriweather, Georgia, serif" text-anchor="middle">
      <text x="358" y="646" font-size="25" font-weight="900">FUND</text>
      <text x="358" y="670" font-size="17">SPV 1</text>
      <text x="602" y="646" font-size="25" font-weight="900">FUND</text>
      <text x="602" y="670" font-size="17">SPV 2</text>
      <text x="800" y="646" font-size="25" font-weight="900">FUND</text>
      <text x="800" y="670" font-size="17">SPV 3</text>
    </g>

    <g fill="var(--orange-soft)">
      <circle cx="264" cy="732" r="42"/>
      <circle cx="505" cy="737" r="42"/>
      <circle cx="747" cy="760" r="42"/>
    </g>
    <g font-family="Merriweather, Georgia, serif" text-anchor="middle" fill="#1c1c1c" font-size="12">
      <text x="264" y="722" font-weight="700" font-size="13">Portfolio:</text>
      <text x="264" y="738">Company</text>
      <text x="264" y="753">or Asset</text>
      <text x="505" y="727" font-weight="700" font-size="13">Portfolio:</text>
      <text x="505" y="743">Company</text>
      <text x="505" y="758">or Asset</text>
      <text x="747" y="750" font-weight="700" font-size="13">Portfolio:</text>
      <text x="747" y="766">Company</text>
      <text x="747" y="781">or Asset</text>
    </g>

    <rect role="img" aria-label="Group of investors" x="362" y="727" width="72" height="26" rx="3" fill="var(--orange-soft)"/>
    <rect role="img" aria-label="Group of investors" x="585" y="727" width="72" height="26" rx="3" fill="var(--orange-soft)"/>
    <rect role="img" aria-label="Group of investors" x="818" y="735" width="72" height="26" rx="3" fill="var(--orange-soft)"/>
  </svg>

  <div class="box ventures">
    <h2>VENTURES</h2>
    <h3>IA Management Group</h3>
    <p>fee on assets of the funds,<br>Plus carried interest</p>
  </div>

  <div class="box website">
    <h2>Website <em>(aka “Funding Platform”)</em></h2>
    <p class="fn-label">Functions:</p>
    <ul class="fn-list"><li>Advertising/Mktg</li><li>SaaS</li></ul>
  </div>

  <div class="box broker">
    <h2>Broker-Dealer -</h2>
    <div class="brand"><span class="brand-mark"></span>CapitalBridge</div>
    <p class="fn-label">Functions:</p>
    <ul class="fn-list"><li>Escrow</li><li>State blue sky</li><li>AML</li><li>Payment processing</li><li>Etc</li></ul>
  </div>

  <div class="fund-label">The Funds:</div>
  <div class="investors-label" style="left:372px;top:757px">Investors</div>
  <div class="investors-label" style="left:594px;top:757px">Investors</div>
  <div class="investors-label" style="left:826px;top:765px">Investors</div>

  <p class="note">* Note: <u>NOT</u> intended as legal advice, consult your securities attorney</p>
  <p class="copyright">©CapitalBridge Technologies, LLC&nbsp; 2015 All Rights Reserved</p>
</div>
</body>
</html>
```